Goals Poster 2023 - Poster design of my goals and those that inspire me!

Hi there!
I'm looking to design a visually beautiful poster to represent my goals for 2023
Here is the info:
https://plinkboard.example/app/board/kT4rWqLm9Zs=/?share_link_id=482913570264
You'll see some examples of designs I like within the file too on the right! Notice the neon colours,but open to other suggestions too.,
I think "The year of No" is important.
And the rules down the bottom are particularly important.
Heres an example of a previous year: https://filevault.example/file/d/93KpRtWnQeLbYcXzVuMaHsDfGjPoT/view
I want to upgrade the overall design from this.
Thanks!
Ned

```html
<!DOCTYPE html>
<html lang="en">
<head>
<meta charset="utf-8">
<title>2023 Goals Poster</title>
<link href="https://fonts.googleapis.com/css2?family=Bowlby+One&family=Oswald:wght@500;600&family=Archivo+Black&family=Teko:wght@400;500&display=swap" rel="stylesheet">
<style>
  :root {
    --ink: #000;
    --paper: #fff;
    --red: #e30613;
    --green: #6ab42e;
    --amber: #b8841e;
  }
  * { margin: 0; padding: 0; box-sizing: border-box; }
  html, body { width: 1200px; height: 1200px; overflow: hidden; background: var(--ink); }
  .poster {
    position: relative; width: 1200px; height: 1200px; overflow: hidden;
    background: var(--ink); color: var(--paper);
    font-family: "Oswald", sans-serif; font-weight: 500;
  }
  .poster > * { position: absolute; }

  .elephant-silhouette {
    left: 30px; top: 200px; width: 1140px; height: 940px;
    background: radial-gradient(closest-side, #1d1d1d 0%, #151515 60%, rgba(0,0,0,0) 100%);
  }

  .year-title {
    left: 64px; top: 42px;
    font-family: "Bowlby One", sans-serif; font-size: 224px; line-height: 1;
    letter-spacing: -12px; color: var(--green);
    text-shadow: 6px 3px 0 var(--amber), 12px 6px 0 var(--red);
  }

  .mission {
    left: 72px; top: 272px; width: 600px;
    font-family: "Teko", sans-serif; font-weight: 400; font-style: italic;
    font-size: 46px; line-height: 40px; letter-spacing: 2px;
    color: var(--red); text-transform: uppercase;
  }

  .side-word {
    writing-mode: vertical-rl; text-orientation: upright; white-space: nowrap;
    font-family: "Oswald", sans-serif; font-weight: 600;
    font-size: 12px; line-height: 1; color: var(--paper);
  }
  .side-word--left { left: 61px; top: 370px; letter-spacing: -1.4px; }
  .side-word--right { left: 1118px; top: 366px; letter-spacing: -5.3px; }

  .banner {
    background: var(--red); color: var(--paper);
    clip-path: polygon(9% 0, 100% 0, 91% 100%, 0 100%);
    display: flex; align-items: center; justify-content: center;
    font-family: "Oswald", sans-serif; font-weight: 600; letter-spacing: 3px;
    text-transform: uppercase;
  }
  .banner--wide { font-family: "Archivo Black", sans-serif; font-weight: 400; }
  .banner--rules {
    left: 805px; top: 42px; width: 315px; height: 44px;
    background: var(--paper); color: var(--red);
    font-family: "Teko", sans-serif; font-style: italic; font-weight: 500;
    font-size: 46px; letter-spacing: 4px; padding-top: 6px;
  }

  .list {
    font-size: 13px; line-height: 17.3px; letter-spacing: 1.4px;
    text-transform: uppercase; list-style: none; white-space: normal;
  }
  .list li { white-space: pre; }
  .list--wide { font-family: "Archivo Black", sans-serif; font-weight: 400; }

  .rules { left: 694px; top: 94px; }

  .no-year { left: 140px; top: 386px; width: 298px; height: 41px; font-size: 21px; }
  .no-year-list { left: 155px; top: 440px; letter-spacing: 1.6px; }

  .branding { left: 132px; top: 605px; width: 311px; height: 41px; font-size: 21px; }
  .branding-list { left: 154px; top: 652px; font-weight: 600; font-size: 12px; line-height: 15.5px; letter-spacing: 1px; }
  .channels { left: 156px; top: 690px; display: flex; }
  .channel { width: 51px; display: flex; flex-direction: column; align-items: center; gap: 1px; }
  .channel-dot { width: 34px; height: 34px; border-radius: 50%; background: var(--paper); }
  .channel-name { font-size: 7px; line-height: 9px; letter-spacing: 0.4px; text-transform: uppercase; white-space: nowrap; }
  .channel-count { font-family: "Teko", sans-serif; font-size: 18px; line-height: 14px; font-style: italic; }

  .community { left: 135px; top: 776px; width: 297px; height: 41px; font-size: 22px; }
  .community-list { left: 162px; top: 825px; font-size: 11px; line-height: 15.5px; letter-spacing: 1.8px; }

  .love { left: 140px; top: 923px; width: 153px; height: 41px; font-size: 23px; }
  .love-list { left: 152px; top: 974px; font-weight: 600; font-size: 15px; line-height: 19px; letter-spacing: 1.1px; }

  .skills { left: 151px; top: 1058px; width: 175px; height: 41px; font-size: 24px; }
  .skills-list { left: 146px; top: 1116px; line-height: 17px; letter-spacing: 1.2px; }

  .fitness { left: 735px; top: 413px; width: 165px; height: 36px; font-size: 21px; }
  .fitness-list { left: 722px; top: 460px; }

  .income { left: 686px; top: 707px; width: 164px; height: 41px; font-size: 21px; }
  .income-list { left: 685px; top: 762px; letter-spacing: 1.2px; }

  .minimal { left: 635px; top: 856px; width: 338px; height: 41px; font-size: 21px; }
  .minimal-list { left: 636px; top: 910px; font-weight: 600; letter-spacing: 1.2px; }

  .spiritual { left: 628px; top: 1051px; width: 254px; height: 41px; font-size: 26px; }
  .spiritual-list { left: 674px; top: 1105px; font-size: 17px; line-height: 20.5px; letter-spacing: 1.8px; }
</style>
</head>
<body>
<main class="poster">
  <div class="elephant-silhouette" role="img" aria-label="Faint dark elephant head silhouette behind the content"></div>

  <h1 class="year-title">2023</h1>
  <p class="mission">Live everyday with integrity and produce an output id admire</p>

  <div class="side-word side-word--left">IMPACT.FITNESS.TOUGHT LEADER.GREAT RELALTIONSHIP</div>
  <div class="side-word side-word--right">FINANCIAL LIBERATED &amp; SUCCESSFUL.BUSINESS.AMAZING COMMUNITY</div>

  <h2 class="banner banner--rules">Yearly Rules</h2>
  <ul class="list rules">
    <li>1. No ClipStream, TV, ReelBox &amp; games unless in the company of Blaze</li>
    <li>2. No social media (possible exception TBD is unless working out</li>
    <li>     by myself )</li>
    <li>3. Get Tessa to post weekly Picturo stories on all my channels</li>
    <li>4. Get Tessa to review message requests on Picturo/Chirper</li>
    <li>5. No eating off plan unless in the company of 4 or more people</li>
    <li>6. No caffeine</li>
    <li>7. No alcohol</li>
    <li>8. No additional projects - unless the total time involment is</li>
    <li>    &lt; 30 hours in 2023 and the business is mission driven. Don't</li>
    <li>    even explore other ideas. You got plenty to work on and solve</li>
    <li>    mate. And I must convince Owen &amp; Dario its worthy of my time.</li>
    <li>9. Audiobooks before bed instead of podcasts.</li>
    <li>10. Only allowed 3 books reading at a time.</li>
    <li>11. Build friends CRM, actively reach out to interesting people</li>
    <li>      every month.</li>
  </ul>

  <h2 class="banner no-year">The year of “No”</h2>
  <ul class="list no-year-list">
    <li>Deep minimalis - remove everything that</li>
    <li>                              can be removed.</li>
    <li>No coaching     - unless I get upside or am generating</li>
    <li>                              content.</li>
    <li>No travel for event -travel ok (w/Clara, see family, building</li>
    <li>                                       my core community, meditation retreat).</li>
    <li>No random rabbit-holes of Chirper, email subscription, etc .</li>
  </ul>

  <h2 class="banner branding">Personal Branding</h2>
  <ul class="list branding-list">
    <li>- Collectively over 500,00 across Chirper, WorkLink, ClipStream &amp; Snapreel</li>
    <li>- 26 videos I'm very proud of.</li>
  </ul>
  <div class="channels">
    <div class="channel"><span class="channel-dot"></span><span class="channel-name">Snapreel</span><span class="channel-count">100k</span></div>
    <div class="channel"><span class="channel-dot"></span><span class="channel-name">ClipStream</span><span class="channel-count">200k</span></div>
    <div class="channel"><span class="channel-dot"></span><span class="channel-name">WorkLink</span><span class="channel-count">75k</span></div>
    <div class="channel"><span class="channel-dot"></span><span class="channel-name">Chirper</span><span class="channel-count">75k</span></div>
    <div class="channel"><span class="channel-dot"></span><span class="channel-name">Picturo</span><span class="channel-count">50k</span></div>
  </div>

  <h2 class="banner banner--wide community">Community</h2>
  <ul class="list list--wide community-list">
    <li>- Hosting brunch every 2weeks</li>
    <li>- Hosting 4 retreats</li>
    <li>      - 2 Nothing Held Back's</li>
    <li>      - 2 Simply Good People</li>
    <li>- Hosting - 4 big events</li>
  </ul>

  <h2 class="banner banner--wide love">Love</h2>
  <ul class="list love-list">
    <li>- Plan a fun date with Clara monthly</li>
    <li>- Tantara exploration</li>
    <li>- Relationship coach</li>
  </ul>

  <h2 class="banner banner--wide skills">Skills</h2>
  <ul class="list skills-list">
    <li>- Learn conversational Swedish</li>
    <li>- DJ at house parties</li>
  </ul>

  <h2 class="banner fitness">Fitness</h2>
  <ul class="list fitness-list">
    <li>- 85kg, 10% BF</li>
    <li>- Follow Groundplan</li>
    <li>- Handstand 30 secs</li>
    <li>- ~2-3 meals per day cooked for me</li>
    <li>   (clear nutrition plan)</li>
    <li>- 90 day no alcohol challenge/</li>
    <li>  transformation</li>
    <li>- Excercise 6 days a week</li>
    <li>- Clear golas with KPIs broekn down</li>
    <li>  by quater and measured on my wall in gym.</li>
    <li>  ( same with friends ).</li>
  </ul>

  <h2 class="banner income">Income</h2>
  <ul class="list income-list">
    <li>- Sold Loudhorn, NW +$XXmil</li>
    <li>- Build~ $XXXmil+ income with Loudhorn US,</li>
    <li>  and minority purchase in cash-flowing assets</li>
    <li>- Start personal brand agency and scale to $XXXk/mo+</li>
  </ul>

  <h2 class="banner minimal">Deep Minimalisation</h2>
  <ul class="list minimal-list">
    <li>- Remove as many as object as possible</li>
    <li>- Close open loops in my brain</li>
    <li>- Remove as many decisions as possible</li>
    <li>- Automate as much as possible</li>
    <li>    - Food, fitness, calendar</li>
    <li>- Limit number of projects allowed</li>
    <li>- Calendar sweep</li>
  </ul>

  <h2 class="banner banner--wide spiritual">Spiritual</h2>
  <ul class="list spiritual-list">
    <li>- Do one meditation retreat</li>
    <li>- Do one Tantara workshop</li>
  </ul>
</main>
</body>
</html>
```